Web Design Project

We wish to create a web based logistics exchange for heavy machinery and equipment catering to the mining, oil, gas and infrastructure industries. Customers interested in shipping equipment can post a load on the site and this would then be auctioned off through an online auction to prospective transport providers.Payments would be through direct bank transfer,kora, brindlepay etc.
Both shippers and transport providers gain access via membership.
When a load is posted it would appear on the map indicating its location.Transport providers click on the icon of this map to access information of the pick up and delivery details as well as the load description.
The site would also have links to transport departments and equipment specification sites.
Advertising and merchandising are the other areas of revenue through the site

Target Market(s)

Shippers from Machinery Auction centres and Transport companies

Industry/Entity Type

Catering

Requirements
Must have
• The Logo of the company. The file is attached.

```html
<!DOCTYPE html>
<html lang="en">
<head>
<meta charset="utf-8">
<title>Tarvella Haulage – Heavy Load Exchange</title>
<link rel="stylesheet" href="https://fonts.googleapis.com/css2?family=Open+Sans:wght@400;600&display=swap">
<style>
:root{
  --page:#e3e3e3;
  --topbar:#3a3a3a;
  --blue:#0b66b8;
  --blue-light:#2a8ee0;
  --blue-dark:#064f96;
  --heading:#1a6db5;
  --text:#444;
  --muted:#9a9a9a;
  --panel:#ffffff;
  --panel-border:#d6dde4;
  --sky:#dcebf7;
  --partner:#b5b5b5;
  --photo-steel:#6f8399;
  --photo-yellow:#c9b13a;
}
*{box-sizing:border-box;margin:0;padding:0}
html,body{width:960px;height:1200px;overflow:hidden}
body{background:var(--page);font-family:"Open Sans",Arial,sans-serif;color:var(--text);position:relative;font-size:11px}
.abs{position:absolute}
.topbar{left:0;top:0;width:960px;height:29px;background:var(--topbar);color:#fff;font-size:11.5px;display:flex;justify-content:flex-end;align-items:center;padding-right:80px;gap:16px}
.brand{left:84px;top:29px;height:44px;display:flex;align-items:center;gap:10px}
.brand-mark{width:40px;height:40px;border-radius:50%;background:var(--blue)}
.brand-name{color:var(--blue);font-size:17px;font-weight:600;letter-spacing:2px;line-height:18px}
.nav{left:81px;top:114px;width:800px;height:52px;background:linear-gradient(var(--blue-light),var(--blue-dark));display:flex}
.nav a{color:#fff;text-decoration:none;font-size:14.5px;display:flex;align-items:center;justify-content:center;border-right:1px solid rgba(255,255,255,.25)}
.nav a:last-child{border-right:none}
.slider{left:90px;top:176px;width:781px;height:246px;border:1px solid #fff;background:linear-gradient(135deg,#5d5a52 0%,var(--photo-steel) 35%,var(--photo-yellow) 65%,#8a8f95 100%)}
.caption{left:0;bottom:0;width:100%;height:69px;background:rgba(40,40,40,.75)}
.caption h2{position:absolute;left:12px;top:10px;font-weight:400;font-size:24px;color:#fff}
.btn{background:linear-gradient(var(--blue-light),var(--blue-dark));color:#fff;font-size:11px;display:inline-flex;align-items:center;justify-content:center;border:1px solid #fff}
.caption .btn{position:absolute;left:13px;top:43px;width:72px;height:19px}
.dots{position:absolute;right:16px;bottom:10px;display:flex;gap:5px}
.dots span{width:7px;height:7px;border-radius:50%;background:#fff}
.dots span:first-child{background:var(--blue);box-shadow:0 0 0 1.5px #fff}
.section-title{color:var(--heading);font-weight:400;font-size:20px}
.thumb{top:469px;width:125px;height:124px;border:2px solid #fff;background:linear-gradient(160deg,#f0f0f0,#c9ad2a 55%,#8c7b2f)}
.thumb .label{position:absolute;left:0;bottom:0;width:100%;height:49px;background:rgba(60,60,60,.75);color:#fff;font-size:11px;line-height:13px;padding:3px 4px}
.map{left:472px;top:457px;width:149px;height:149px;border:2px solid #fff;background:linear-gradient(135deg,#eef0e2,#dfe3d0 50%,#e9e3c8)}
.read{top:601px;width:68px;height:19px}
.panel{background:var(--panel);border:1px solid var(--panel-border)}
.welcome h1{font-weight:400;font-size:19px;color:var(--heading);position:absolute;left:7px;top:2px}
.welcome p{position:absolute;left:7px;width:500px;font-size:10.4px;line-height:14.5px;color:#555}
.small-title{position:absolute;left:5px;top:5px;font-size:11.5px;color:#333;white-space:nowrap}
.bid-list{position:absolute;left:3px;top:30px;color:var(--blue);font-size:8.8px;line-height:14.5px;white-space:nowrap}
.quote-row{position:absolute;left:5px;width:115px;display:flex;justify-content:space-between;font-size:9px;font-style:italic;color:var(--muted)}
.mini-btn{position:absolute;right:4px;width:46px;height:11px;font-size:8px}
.form-row{position:absolute;left:5px;display:flex;align-items:center;font-size:8.8px;line-height:11px;color:#333}
.form-row span:first-child{width:62px}
.form-row span:last-child{font-style:italic;color:var(--muted);font-size:7.5px}
.box{position:absolute;border:1px solid #ccc;background:#fff;font-size:7px;line-height:8px;color:#555;padding:2px}
.tabs{left:91px;top:801px;width:518px;height:192px;background:linear-gradient(var(--sky),#fff 60%);border:1px solid var(--panel-border)}
.tab{position:absolute;top:0;height:45px;font-size:19px;color:var(--heading);display:flex;align-items:center;padding-left:8px}
.col{position:absolute;top:52px;width:240px;color:#444}
.col h3{font-weight:400;font-size:13px;line-height:15px;color:#222}
.col p{margin-top:10px;width:228px;font-size:10.4px;line-height:14.5px;color:#555}
.partner{position:absolute;background:var(--partner);border-radius:2px}
.footer{left:81px;top:1122px;width:800px;height:53px;background:linear-gradient(var(--blue-light),var(--blue-dark));color:#fff}
.footer-nav{position:absolute;left:8px;top:19px;display:flex;font-size:9.6px}
.footer-nav span{padding:0 13px;border-left:1px solid #fff}
.footer-nav span:first-child{padding-left:0;border-left:none}
.social{position:absolute;left:544px;top:19px;display:flex;gap:4px}
.social span{width:18px;height:18px;background:#fff;opacity:.85;border-radius:2px}
.legal{position:absolute;right:6px;top:25px;text-align:right;font-size:9.6px;line-height:13px}
</style>
</head>
<body>
<div class="abs topbar"><span>Contact</span><span>|</span><span>Help</span><span>|</span><span>Member login</span></div>
<div class="abs brand"><span class="brand-mark"></span><span class="brand-name">TARVELLA<br>HAULAGE</span></div>

<nav class="abs nav">
  <a style="width:88px">Home</a><a style="width:89px">Services</a><a style="width:93px">Storage</a>
  <a style="width:125px">How it works</a><a style="width:102px">Solutions</a><a style="width:71px">FAQ</a>
  <a style="width:121px">Testimonials</a><a style="width:111px">About Us</a>
</nav>

<section class="abs slider" role="img" aria-label="Photo of a heavy haulage truck convoy carrying oversized equipment">
  <div class="abs caption">
    <h2>One Stop Solution for all your transportation needs</h2>
    <span class="btn">Learn more</span>
    <div class="dots"><span></span><span></span><span></span><span></span><span></span></div>
  </div>
</section>

<h2 class="abs section-title" style="left:97px;top:434px">Recent projects open for bidding</h2>

<div class="abs thumb" style="left:90px" role="img" aria-label="Photo of excavator machinery"><div class="label">Noida<br>to<br>Delhi</div></div>
<div class="abs thumb" style="left:221px" role="img" aria-label="Photo of excavator machinery"><div class="label">Noida<br>to<br>Delhi</div></div>
<div class="abs thumb" style="left:353px" role="img" aria-label="Photo of excavator machinery"><div class="label">Noida<br>to<br>Delhi</div></div>
<div class="abs map" role="img" aria-label="Route map from New Delhi to Noida"></div>
<div class="abs thumb" style="left:622px" role="img" aria-label="Photo of excavator machinery"><div class="label">Noida<br>to<br>Delhi</div></div>
<div class="abs thumb" style="left:749px" role="img" aria-label="Photo of excavator machinery"><div class="label">Noida<br>to<br>Delhi</div></div>

<span class="abs btn read" style="left:117px">Read More</span>
<span class="abs btn read" style="left:249px">Read More</span>
<span class="abs btn read" style="left:384px">Read More</span>
<span class="abs btn read" style="left:517px">Read More</span>
<span class="abs btn read" style="left:642px">Read More</span>
<span class="abs btn read" style="left:770px">Read More</span>

<section class="abs panel welcome" style="left:90px;top:632px;width:519px;height:133px">
  <h1>Welcome to Tarvella Haulage...</h1>
  <p style="top:39px">This is Draftline's version&nbsp; of Lorem Ipsum. Proin gravida nibh vel velit auctor aliquet. Aenean sollicitudin, lorem quis bibendum auctor, nisi elit consequat ipsum, nec sagittis sem nibh id elit. Duis sed odio sit amet nibh vulputate cursus a sit amet mauris.</p>
  <p style="top:96px">Morbi accumsan ipsum velit. Nam nec tellus a odio tincidunt auctor a ornare odio. Sed non&nbsp; mauris vitae erat consequat auctor eu in elit. Class aptent taciti sociosqu ad litora torquent per conubia</p>
</section>
<span class="abs btn" style="left:544px;top:767px;width:67px;height:19px;font-size:12px">Read More</span>

<section class="abs panel" style="left:617px;top:632px;width:125px;height:131px">
  <div class="small-title">Running bid Projects</div>
  <div class="bid-list">This is Draftline's version.<br>Ofdium Lorem Ipsum.<br>Gravida nibh vel velit.<br>Aliquet. Aenean sollicitudin,<br>Lorem quis bibendum.</div>
  <span class="btn mini-btn" style="top:117px">View All</span>
</section>

<section class="abs panel" style="left:748px;top:632px;width:126px;height:131px">
  <div class="small-title">Submit Quote <span style="font-size:6.5px">Open/Closed</span></div>
  <div class="quote-row" style="top:36px"><span>Name</span><span>Price/Kms</span></div>
  <div class="quote-row" style="top:50px"><span>Name</span><span>Price/Kms</span></div>
  <div class="quote-row" style="top:64px"><span>Name</span><span>Price/Kms</span></div>
  <div class="quote-row" style="top:78px"><span>Name</span><span>Price/Kms</span></div>
  <div class="quote-row" style="top:92px"><span>Name</span><span>Price/Kms</span></div>
  <span class="btn mini-btn" style="top:117px">Submit</span>
</section>

<section class="abs panel" style="left:617px;top:771px;width:257px;height:96px">
  <div class="small-title" style="color:var(--heading);font-size:11.5px;font-weight:600">Launch Bid Project</div>
  <div class="form-row" style="top:24px"><span>Source :</span><span>Source Station</span></div>
  <div class="form-row" style="top:38px"><span>Destination</span><span>Delivery Point</span></div>
  <div class="form-row" style="top:52px"><span>Load :</span><span>4000kgs</span></div>
  <div class="form-row" style="top:66px"><span>Quality :</span><span>Solid(Heavy) ▾</span></div>
  <div class="form-row" style="top:80px"><span>Time limit :</span><span>15 Days</span></div>
  <div class="box" style="left:131px;top:2px;width:123px;height:49px">This is Draftline's version of Lorem Ipsum. Proin gravida nibh vel velit auctor aliquet. Aenean sollicitudin, lorem quis bibendum auctor...</div>
  <div class="box" style="left:131px;top:54px;width:123px;height:19px;font-size:7.5px">Address &amp; contact Info.</div>
  <span class="btn mini-btn" style="top:82px">Submit</span>
</section>

<section class="abs" style="left:618px;top:873px;width:255px;height:119px;background:linear-gradient(var(--sky),#eef5fb);border:1px solid var(--panel-border)">
  <div style="position:absolute;left:7px;top:4px;font-size:14px;color:#222">Payment</div>
</section>

<section class="abs tabs">
  <div class="tab" style="left:0;width:130px;background:var(--sky)">Why US ??</div>
  <div class="tab" style="left:130px;width:169px;background:#f3f3f3;border-left:1px solid #fff">Take a Quick Tour</div>
  <div class="col" style="left:11px">
    <h3>This is Draftline's version&nbsp; of Lorem Ipsum.</h3>
    <p>&nbsp;Proin gravida nibh vel velit auctor aliquet. Aenean sollicitudin, lorem quis bibendum auctor, nisi elit consequat ipsum, nec sagittis sem nibh id elit. Duis sed odio sit amet nibh vulputate cursus a sit amet mauris. Morbi accumsan ipsum velit. Nam nec tellus a odio</p>
  </div>
  <div class="col" style="left:268px">
    <h3>This is Draftline's version&nbsp; of Lorem Ipsum.</h3>
    <p>&nbsp;Proin gravida nibh vel velit auctor aliquet. Aenean sollicitudin, lorem quis bibendum auctor, nisi elit consequat ipsum, nec sagittis sem nibh id elit. Duis sed odio sit amet nibh vulputate cursus a sit amet mauris. Morbi accumsan ipsum velit. Nam nec tellus a odio</p>
  </div>
</section>

<h2 class="abs section-title" style="left:90px;top:1015px">Our Partners</h2>
<div class="abs partners" style="left:0;top:0" aria-label="Partner badges">
  <span class="partner" style="left:97px;top:1046px;width:61px;height:18px"></span>
  <span class="partner" style="left:174px;top:1049px;width:34px;height:11px"></span>
  <span class="partner" style="left:222px;top:1048px;width:48px;height:16px"></span>
  <span class="partner" style="left:281px;top:1048px;width:78px;height:14px"></span>
  <span class="partner" style="left:368px;top:1050px;width:23px;height:20px"></span>
  <span class="partner" style="left:403px;top:1049px;width:24px;height:22px"></span>
  <span class="partner" style="left:437px;top:1052px;width:73px;height:16px"></span>
  <span class="partner" style="left:299px;top:1074px;width:38px;height:8px"></span>
  <span class="partner" style="left:122px;top:1077px;width:61px;height:18px"></span>
  <span class="partner" style="left:198px;top:1080px;width:56px;height:19px"></span>
  <span class="partner" style="left:264px;top:1084px;width:38px;height:13px"></span>
  <span class="partner" style="left:326px;top:1090px;width:35px;height:10px"></span>
  <span class="partner" style="left:369px;top:1083px;width:53px;height:13px"></span>
  <span class="partner" style="left:470px;top:1085px;width:76px;height:17px"></span>
  <span class="partner" style="left:565px;top:1073px;width:83px;height:13px"></span>
  <span class="partner" style="left:655px;top:1052px;width:73px;height:16px"></span>
  <span class="partner" style="left:688px;top:1085px;width:76px;height:17px"></span>
  <span class="partner" style="left:782px;top:1073px;width:84px;height:13px"></span>
</div>

<footer class="abs footer">
  <div class="footer-nav"><span>Home</span><span>Services</span><span>Storage</span><span>How it works</span><span>Solutions</span><span>FAQ</span><span>Testimonials</span><span>About Us</span></div>
  <div class="social" aria-label="Social links"><span></span><span></span><span></span><span></span><span></span></div>
  <div class="legal">Copy right reserved<br>Privacy Policy | Contact Us</div>
</footer>
</body>
</html>
```